Etikett für Likörflasche - Moonshine
Zielgruppe
Wir sind eine kleine Moonshine / Likörmanufaktur. Unser Obst für die Brände und Liköre stammt aus eigenem Anbau bzw. von umliegenden regionalen Bauern. Hier setzen wir auf sehr gute Qualität und verwenden keine Zusatzstoffe, Geschmacksverstärker, Farbstoffe etc. Im ersten Schritt werden wir nur 3-4 verschiedene Liköre anbieten.
Wir möchten unsere Liköre zukünftig auf Veranstaltungen / Events und Märkten verkaufen. Hierfür suchen wir ein pfiffiges und ansprechendes Etikettendesign.
Das Wort 'Moonshine' soll die Leute auf den Events zu uns führen. Das wird auch mit großen Fahnen am Verkaufsstand beworben. Da wir auch ein paar amerikanische Foodtrucks haben soll auch das Etikett ein bisschen amerikanisch gehalten werden.
Zielgruppe: 28 bis 55 Jahre (Männer & Frauen)
Verkaufspreis pro 0,5 Liter Flasche ca. 24,50 Euro
Aufgabenstellung
Es soll ein Etikett auf die Flasche (nur vorne nicht auf die Rückseite).
Etikettengröße: ca. 7,0 x 8,5cm (für die 0,5l Flasche)
Angaben die sich auf dem Etikett ändern:
- Inhalt entweder 0,35l oder 0,5l Flasche
- Bezeichnung vom Inhalt und 'Kurzbeschreibung'
- Alkoholgehalt
Ich habe in PowerPoint schon mal ein Etikett zusammen gestellt, auf dem die Angaben alle mit enthalten sind. Hier fehlt mir allerdings der Pfiff und das Professionelle. Auch die Darstellung der Eigenschaften wie 'Echte Früchte', 'Handcrafted' etc. gefällt mir so auch nicht. Vielleicht wäre auch noch ein cooler Spruch darauf gut.
In die Anlage habe ich meine kreierte PowerPoint Folie gepackt (auf der 2. Folie findet ihr die geplante Flasche in die abgefüllt wird). Die zweite Datei ist ein Design was meinen Vorstellungen schon gut nahe kommt aus dem Internet (hier gefallen mir die Linien, kleine Gimmicks etc. da passiert einfach was auf dem Etikett). Von der Art her würde mir dieser Style gut gefallen. Es soll nur nicht zu überladen und kitschig werden.
Likörsorten die es geben wird: Wir werden uns erstmal auf 3-4 Sorten beschränken.

```html
<!DOCTYPE html>
<html lang="de">
<head>
<meta charset="utf-8">
<title>Marlow Moonshine – Etikett</title>
<link href="https://fonts.googleapis.com/css2?family=Josefin+Sans:wght@300;400;600&display=swap" rel="stylesheet">
<style>
  :root {
    --backdrop: #ececee;
    --paper: #f3f2f0;
    --wine: #8c2a2a;
    --ink-grey: #6e6e6e;
    --rule-grey: #cfcfcf;
  }
  * { box-sizing: border-box; margin: 0; padding: 0; }
  html, body {
    width: 1200px; height: 900px; overflow: hidden;
    background: var(--backdrop);
  }
  .canvas {
    width: 1200px; height: 900px;
    display: flex; align-items: center; justify-content: center;
  }
  .label {
    position: relative; width: 470px; height: 570px;
    background: var(--paper);
    border: 7px solid var(--wine);
  }
  .label__inner-rule {
    position: absolute; inset: 7px;
    border: 1.5px solid var(--wine);
    pointer-events: none;
  }
  .label__content {
    position: absolute; inset: 0;
    display: flex; flex-direction: column; align-items: center;
    justify-content: space-between;
    padding: 70px 40px 64px;
  }
  .brand-block { display: flex; flex-direction: column; align-items: center; }
  .brand {
    display: flex; align-items: center; gap: 14px;
    font-family: "Josefin Sans", sans-serif; font-weight: 600;
    font-size: 40px; line-height: 1; letter-spacing: 3px;
    color: var(--wine);
  }
  .brand__mark {
    width: 14px; height: 14px; background: var(--wine); flex: none;
  }
  .divider-dash {
    width: 30px; height: 5px; background: var(--rule-grey);
    margin-top: 34px;
  }
  .product-block { display: flex; flex-direction: column; align-items: center; }
  .product-name {
    font-family: "Josefin Sans", sans-serif; font-weight: 400;
    font-size: 28px; line-height: 1.25; letter-spacing: 3px;
    color: var(--wine); text-align: center;
  }
  .description {
    margin-top: 20px; border: 1px solid var(--wine);
    padding: 7px 14px 5px; text-align: center;
    font-family: "Josefin Sans", sans-serif; font-weight: 400;
    font-size: 11px; letter-spacing: 1.6px; line-height: 1.45;
    color: var(--ink-grey);
  }
  .facts-block { display: flex; flex-direction: column; align-items: center; width: 340px; }
  .rule-band { width: 100%; height: 3px; background: var(--rule-grey); }
  .facts {
    width: 100%; margin: 12px 0;
    display: flex; justify-content: space-between;
    font-family: "Josefin Sans", sans-serif; font-weight: 400;
    font-size: 15px; letter-spacing: 1.5px; color: var(--wine);
  }
</style>
</head>
<body>
<main class="canvas">
  <section class="label" aria-label="Flaschenetikett Marlow Moonshine, Bramble and Oak">
    <div class="label__inner-rule"></div>
    <div class="label__content">
      <div class="brand-block">
        <h1 class="brand"><span class="brand__mark"></span>MARLOW MOONSHINE</h1>
        <div class="divider-dash"></div>
      </div>
      <div class="product-block">
        <h2 class="product-name">BRAMBLE<br>AND OAK</h2>
        <p class="description">WILDE BEEREN TREFFEN AUF VIELSCHICHTIGE<br>NOTEN VON WHISKEY UND KARAMELL</p>
      </div>
      <div class="facts-block">
        <div class="rule-band"></div>
        <div class="facts">
          <span>500 ML</span>
          <span>22 % VOL</span>
          <span>44 PROOF</span>
        </div>
        <div class="rule-band"></div>
      </div>
    </div>
  </section>
</main>
</body>
</html>
```